Business card for dental office with laser therapy / dental facial esthetic

A simple logo which should signifies
Dentistry intraoral as primary and with extended extraoral cosmetic facial esthetic services ( regenerative skincare ) which enhance Beauty as whole .
Conservative high tech approach by using laser intraoral and extraoral limited to face and neck
Front Face :May be black background with neon blue / purplish Rim signifies laser ( ?) & abstract face profile and tooth or Apple design in one ? / see upload inspiration design
Back side : simple appointment slots with date and time / white background / black letter

Color : black/ neon blue/ purplish and gold incorporate for logo design
Final design : dental / esthetic / modern high tech and safe

Target Market(s)

Dental Patients who seeks more high end cosmetic treatment

Industry/Entity Type

Health Care

Contact Information for Business Card

Esthetic modern elegant looking
Logo and office must haves important informations

Logo Text

Family & Cosmetic Dentistry

Font styles to use
Script

Requirements
Must have
• Name of practice and all important informations
• Family & Cosmetic Dentistry
• Lan M. Trieu DMD,PC
• 38472 Orbury Court ,ste.217
• Larkmoor Hills ,VA 20931
• Ph. 555-319-8270
• Fax 555-3195714
Nice to have
• More abstract
• Front : black back ground with neon blue rim (signifies laser therapy)
• Logo can also be golden gold / neon blue
• Address & Infos can be white
Should not have
• Not to busy looking

```html
<!DOCTYPE html>
<html lang="en">
<head>
<meta charset="utf-8">
<title>Family &amp; Cosmetic Dentistry – Business Card</title>
<link href="https://fonts.googleapis.com/css2?family=Open+Sans:wght@400;600&display=swap" rel="stylesheet">
<style>
  :root {
    --backdrop: #24272c;
    --card: #0b0b0c;
    --card-edge: #151618;
    --neon-blue: #3fb3d9;
    --rim-blue: #2fa3d0;
    --text-white: #e9ecef;
    --text-soft: #c9ced3;
  }
  * { box-sizing: border-box; margin: 0; padding: 0; }
  html, body {
    width: 1200px; height: 900px; overflow: hidden;
    background: var(--backdrop);
    font-family: "Open Sans", Arial, sans-serif;
  }
  .canvas {
    position: relative; width: 1200px; height: 900px;
    display: flex; flex-direction: column; align-items: center; justify-content: center; gap: 36px;
  }
  .card {
    position: relative; width: 640px; height: 366px;
    background: var(--card);
    border-radius: 28px;
    box-shadow: 0 18px 40px rgba(0,0,0,0.45);
    overflow: hidden;
  }
  /* Front side: practice name only */
  .card--front { display: flex; align-items: center; justify-content: center; }
  .practice-name {
    display: flex; align-items: center; gap: 16px;
  }
  .practice-name__dot {
    width: 30px; height: 30px; border-radius: 50%; background: var(--neon-blue);
    flex: none;
  }
  .practice-name__text {
    color: var(--text-white); font-size: 30px; font-weight: 400; letter-spacing: 0.5px;
    line-height: 1.15;
  }
  /* Back side: contact details */
  .card--details { border-left: 10px solid var(--rim-blue); }
  .holder {
    position: absolute; left: 44px; top: 40px;
  }
  .holder__name { color: var(--text-white); font-size: 30px; font-weight: 400; }
  .holder__title { color: var(--neon-blue); font-size: 13px; font-weight: 600; margin-top: 2px; }
  .divider {
    position: absolute; left: 44px; top: 112px; width: 300px; height: 1.5px;
    background: var(--neon-blue);
  }
  .contacts {
    position: absolute; left: 44px; top: 168px; list-style: none;
    color: var(--text-soft); font-size: 13px;
  }
  .contacts li { display: flex; align-items: center; gap: 8px; margin-bottom: 8px; }
  .contacts svg { width: 13px; height: 13px; flex: none; }
  .practice-name--small { position: absolute; right: 40px; top: 130px; gap: 12px; }
  .practice-name--small .practice-name__dot { width: 22px; height: 22px; }
  .practice-name--small .practice-name__text { font-size: 21px; }
  .address {
    position: absolute; right: 40px; bottom: 44px; text-align: right;
    color: var(--text-soft); font-size: 15px; line-height: 1.5; font-style: normal;
  }
</style>
</head>
<body>
<main class="canvas">
  <section class="card card--front" aria-label="Card front">
    <div class="practice-name">
      <span class="practice-name__dot"></span>
      <span class="practice-name__text">Family &amp; Cosmetic Dentistry</span>
    </div>
  </section>

  <section class="card card--details" aria-label="Card back">
    <div class="holder">
      <p class="holder__name">Lan M. Trieu</p>
      <p class="holder__title">DMD,PC</p>
    </div>
    <div class="divider"></div>
    <ul class="contacts">
      <li>
        <svg viewBox="0 0 16 16" aria-hidden="true"><path d="M4 1.5c.6 0 1 .4 1.2 1l.8 2.3c.2.5 0 1-.4 1.3L4.5 7c.8 1.8 2.3 3.3 4.1 4.2l.9-1.1c.3-.4.9-.6 1.3-.4l2.3.8c.6.2 1 .7 1 1.2v1.8c0 .8-.7 1.5-1.5 1.5C6.5 15 1 9.5 1 3c0-.8.7-1.5 1.5-1.5z" fill="var(--neon-blue)"/></svg>
        555-319-8270
      </li>
      <li>
        <svg viewBox="0 0 16 16" aria-hidden="true"><rect x="4" y="1.5" width="8" height="4" fill="none" stroke="var(--neon-blue)" stroke-width="1.4"/><rect x="1.5" y="5.5" width="13" height="6.5" rx="1" fill="var(--neon-blue)"/><rect x="4" y="10" width="8" height="4.5" fill="var(--card)" stroke="var(--neon-blue)" stroke-width="1.4"/></svg>
        555-3195714
      </li>
    </ul>
    <div class="practice-name practice-name--small">
      <span class="practice-name__dot"></span>
      <span class="practice-name__text">Family &amp; Cosmetic<br>Dentistry</span>
    </div>
    <address class="address">
      38472 Orbury Court ,ste.217<br>
      Larkmoor Hills ,VA 20931
    </address>
  </section>
</main>
</body>
</html>
```